Business Card Design

Lanternfield Recruitment is a specialist financial services recruitment company and implementation partner

Industry/Entity Type

Business

Contact Information for Business Card

Tom Hadley
Lanternfield Recruiment Ltd
e:tom.hadley@lanternfield-recruitment.example
m:07723 408 316
m:07844 251 903
s: tommhadley

```html
<!DOCTYPE html>
<html lang="en">
<head>
<meta charset="utf-8">
<title>Lanternfield Recruitment – Business Card</title>
<link rel="stylesheet" href="https://fonts.googleapis.com/css2?family=Cinzel:wght@500;600&display=swap">
<style>
  :root {
    --paper: #ffffff;
    --ink: #111111;
    --rule: #121212;
    --band: #00ffff;
    --mark: #1f2a33;
  }
  html, body {
    margin: 0;
    padding: 0;
    width: 1200px;
    height: 720px;
    overflow: hidden;
    background: var(--paper);
  }
  .card {
    position: relative;
    width: 1200px;
    height: 720px;
    background: var(--paper);
    font-family: "Cinzel", "Trajan Pro", serif;
    color: var(--ink);
  }
  .tagline {
    position: absolute;
    top: 84px;
    left: 0;
    width: 1200px;
    margin: 0;
    text-align: center;
    font-size: 35px;
    font-weight: 600;
    letter-spacing: 0.2px;
    line-height: 1;
  }
  .rule {
    position: absolute;
    left: 0;
    width: 1200px;
    height: 12px;
    background: var(--rule);
  }
  .rule--top { top: 165px; }
  .rule--bottom { top: 542px; }
  .brand-band {
    position: absolute;
    top: 177px;
    left: 0;
    width: 1200px;
    height: 365px;
    background: var(--band);
    display: flex;
    align-items: center;
    justify-content: center;
  }
  .brand-name {
    margin: 0;
    font-size: 54px;
    font-weight: 600;
    color: var(--mark);
    letter-spacing: 1px;
  }
  .services {
    position: absolute;
    top: 567px;
    left: 0;
    width: 1200px;
    margin: 0;
    padding: 0;
    list-style: none;
    text-align: center;
    font-size: 31px;
    font-weight: 600;
    line-height: 37px;
  }
  .services .sep {
    display: inline-block;
    width: 0;
    height: 0;
    margin: 0 12px 6px 10px;
    border-top: 4px solid transparent;
    border-bottom: 4px solid transparent;
    border-left: 6px solid var(--ink);
    vertical-align: middle;
  }
</style>
</head>
<body>
  <div class="card">
    <p class="tagline">Specialists in Payments and Core Banking Talent</p>
    <div class="rule rule--top"></div>
    <div class="brand-band">
      <p class="brand-name">Lanternfield Recruitment</p>
    </div>
    <div class="rule rule--bottom"></div>
    <ul class="services">
      <li>Core Banking Payments<span class="sep"></span>Cash Management and Trade</li>
      <li>Treasury and Capital Markets</li>
      <li>Governance<span class="sep"></span>Risk and Compliance</li>
    </ul>
  </div>
</body>
</html>
```